Seeking creative design for partial wrap on bakery truck selling homemade Pies

Create a partial eye catching wrap for my food truck selling pies

We sell pies for such as apple cherry pumpkin ect Were located in nashville Tn and would like to include that in theme

This is a partial design on a R370 bus

Target Market(s)

People at Fairs and other events locally that like sweets

Industry/Entity Type

Food Trucks

Font styles to use
Decorative
Script

Requirements
Must have
• Name : www. Maplebrook Bakes . Com And Pictures of pies and nashville based theme

```html
<!DOCTYPE html>
<html lang="en">
<head>
<meta charset="utf-8">
<title>Maplebrook Bakes Co – Bus Wrap</title>
<link rel="stylesheet" href="https://fonts.googleapis.com/css2?family=Josefin+Sans:wght@400;700&family=Sacramento&family=Fredoka:wght@600&display=swap">
<style>
  :root{
    --wrap-blue:#2f52a6;
    --ray-blue:#8d93cf;
    --phone-red:#e2463c;
    --line:#3a3a3a;
    --tire:#0d0d0d;
    --rim:#c4c4c4;
    --arch:#555555;
    --glass:#aee0f7;
    --bumper:#8a8a8a;
    --pie-light:#d8c08a;
    --pie-dark:#9a7a45;
    --paper:#ffffff;
  }
  html,body{margin:0;padding:0;overflow:hidden;background:var(--paper);}
  .canvas{width:1200px;height:720px;display:block;}
  .site-url{font-family:"Josefin Sans",sans-serif;font-weight:400;fill:var(--wrap-blue);letter-spacing:2px;}
  .phone{font-family:"Fredoka",sans-serif;font-weight:600;fill:var(--phone-red);}
  .phone--light{fill:var(--paper);}
  .brand-name{font-family:"Josefin Sans",sans-serif;font-weight:700;fill:var(--wrap-blue);letter-spacing:3px;}
  .tagline{font-family:"Josefin Sans",sans-serif;font-weight:400;fill:var(--paper);letter-spacing:1px;}
  .tagline-script{font-family:"Sacramento",cursive;fill:var(--paper);}
  .social-handle{font-family:"Josefin Sans",sans-serif;font-weight:700;fill:var(--paper);}
  .body-shell{fill:var(--paper);stroke:var(--line);stroke-width:2;}
  .outline{fill:none;stroke:var(--line);stroke-width:2;}
  .window{fill:none;stroke:var(--line);stroke-width:2;}
  .wrap-blue{fill:var(--wrap-blue);}
  .tire{fill:var(--tire);}
  .rim{fill:var(--rim);stroke:var(--tire);stroke-width:6;}
  .hub{fill:var(--rim);stroke:var(--tire);stroke-width:6;}
  .arch{fill:var(--arch);}
  .black{fill:var(--tire);}
  .tail-light{fill:var(--phone-red);}
</style>
</head>
<body>
<svg class="canvas" viewBox="0 0 2480 1488" preserveAspectRatio="xMidYMid meet" xmlns="http://www.w3.org/2000/svg">
  <defs>
    <radialGradient id="ray-glow" cx="0.35" cy="0.4" r="0.7">
      <stop offset="0" stop-color="#ffffff"/>
      <stop offset="0.55" stop-color="#c9cbea"/>
      <stop offset="1" stop-color="#ffffff"/>
    </radialGradient>
    <radialGradient id="ray-glow-rear" cx="0.5" cy="0.55" r="0.7">
      <stop offset="0" stop-color="#ffffff"/>
      <stop offset="0.6" stop-color="#c2c5e8"/>
      <stop offset="1" stop-color="#e8e9f6"/>
    </radialGradient>
    <radialGradient id="pie-tone" cx="0.5" cy="0.45" r="0.6">
      <stop offset="0" stop-color="var(--pie-light)"/>
      <stop offset="1" stop-color="var(--pie-dark)"/>
    </radialGradient>
    <clipPath id="rear-box-clip">
      <path d="M195,120 L960,120 L960,510 L195,510 Z"/>
    </clipPath>
  </defs>

  <!-- Side view: passenger side (upper) -->
  <g class="bus-side bus-side--passenger">
    <path class="body-shell" d="M195,120 L1110,125 L1170,145 L1170,210 L1150,215 L1150,240 L1250,335 L1395,360 L1410,400 L1420,450 L1420,505 L1370,512 L195,510 Z"/>
    <g clip-path="url(#rear-box-clip)">
      <rect x="195" y="118" width="765" height="300" fill="url(#ray-glow)" opacity="0.85"/>
      <rect x="600" y="118" width="360" height="300" fill="#ffffff" opacity="0.6"/>
      <path class="wrap-blue" d="M195,322 Q480,318 600,400 Q700,470 830,512 L195,512 Z"/>
    </g>
    <g class="windows">
      <rect class="window" x="230" y="175" width="100" height="152" rx="14"/>
      <rect class="window" x="355" y="175" width="100" height="152" rx="14"/>
      <rect class="window" x="480" y="175" width="100" height="152" rx="14"/>
      <rect class="window" x="605" y="175" width="100" height="152" rx="14"/>
      <rect class="window" x="730" y="175" width="100" height="152" rx="14"/>
      <rect class="window" x="855" y="175" width="100" height="152" rx="14"/>
    </g>
    <line class="outline" x1="960" y1="120" x2="960" y2="512"/>
    <line class="outline" x1="195" y1="402" x2="960" y2="402"/>
    <rect class="outline" x="985" y="162" width="160" height="356"/>
    <rect class="outline" x="1003" y="185" width="45" height="325"/>
    <rect class="outline" x="1080" y="185" width="45" height="325"/>
    <path class="outline" d="M1160,285 L1205,335 L1205,450 L1170,452 L1158,440 Z"/>
    <rect class="black" x="1358" y="265" width="28" height="65" rx="6"/>
    <path class="black" d="M1350,355 L1380,345 L1375,385 L1358,388 Z"/>
    <rect class="tail-light" x="190" y="390" width="8" height="40"/>
    <rect class="black" x="178" y="458" width="35" height="30"/>
    <path class="black" d="M1360,450 L1420,450 L1420,490 L1400,508 L1365,508 Z"/>
    <path class="arch" d="M482,510 L482,455 Q560,425 640,445 L650,510 Z"/>
    <path class="arch" d="M1210,500 Q1230,420 1300,420 Q1350,425 1365,460 L1365,500 Z"/>
    <circle class="tire" cx="563" cy="515" r="62"/>
    <circle class="rim" cx="563" cy="515" r="42"/>
    <circle class="hub" cx="563" cy="515" r="18"/>
    <circle class="tire" cx="1294" cy="515" r="62"/>
    <circle class="rim" cx="1294" cy="515" r="42"/>
    <circle class="hub" cx="1294" cy="515" r="18"/>

    <ellipse cx="520" cy="388" rx="60" ry="62" fill="url(#pie-tone)" role="img" aria-label="Photo of golden hand pies"/>
    <text class="site-url" x="812" y="156" font-size="31" text-anchor="middle">MAPLEBROOKBAKES.COM</text>
    <text class="phone" x="790" y="392" font-size="44" text-anchor="middle">(555) 014-0199</text>
    <text class="brand-name" x="385" y="248" font-size="34" text-anchor="middle">MAPLEBROOK</text>
    <text class="brand-name" x="385" y="290" font-size="34" text-anchor="middle">BAKES CO</text>
    <text class="tagline" x="330" y="386" font-size="15" text-anchor="middle">GOURMET PIES WITH A</text>
    <text class="tagline-script" x="330" y="418" font-size="40" text-anchor="middle">Southern Charm</text>
    <rect x="362" y="446" width="20" height="20" fill="var(--paper)"/>
    <text class="social-handle" x="390" y="463" font-size="17">@maplebrook</text>
  </g>

  <!-- Side view: driver side (lower) -->
  <g class="bus-side bus-side--driver">
    <g transform="translate(1600,655) scale(-1,1)">
      <path class="body-shell" d="M195,120 L1110,125 L1170,145 L1170,210 L1150,215 L1150,240 L1250,335 L1395,360 L1410,400 L1420,450 L1420,505 L1370,512 L195,510 Z"/>
      <g clip-path="url(#rear-box-clip)">
        <rect x="195" y="118" width="765" height="300" fill="url(#ray-glow)" opacity="0.85"/>
        <rect x="600" y="118" width="360" height="300" fill="#ffffff" opacity="0.6"/>
        <path class="wrap-blue" d="M195,322 Q480,318 600,400 Q700,470 830,512 L195,512 Z"/>
      </g>
      <g class="windows">
        <rect class="window" x="230" y="175" width="100" height="152" rx="14"/>
        <rect class="window" x="355" y="175" width="100" height="152" rx="14"/>
        <rect class="window" x="480" y="175" width="100" height="152" rx="14"/>
        <rect class="window" x="605" y="175" width="100" height="152" rx="14"/>
        <rect class="window" x="730" y="175" width="100" height="152" rx="14"/>
        <rect class="window" x="855" y="175" width="100" height="152" rx="14"/>
        <line class="outline" x1="230" y1="215" x2="955" y2="215"/>
      </g>
      <line class="outline" x1="960" y1="120" x2="960" y2="512"/>
      <line class="outline" x1="195" y1="402" x2="960" y2="402"/>
      <rect class="outline" x="1045" y="250" width="180" height="245"/>
      <path class="outline" d="M1160,285 L1205,335 L1205,450 L1170,452 L1158,440 Z"/>
      <rect class="black" x="1358" y="265" width="28" height="110" rx="6"/>
      <rect class="tail-light" x="190" y="390" width="8" height="40"/>
      <rect class="black" x="178" y="458" width="35" height="30"/>
      <path class="black" d="M1360,450 L1420,450 L1420,490 L1400,508 L1365,508 Z"/>
      <path class="arch" d="M482,510 L482,455 Q560,425 640,445 L650,510 Z"/>
      <path class="arch" d="M1210,500 Q1230,420 1300,420 Q1350,425 1365,460 L1365,500 Z"/>
      <circle class="tire" cx="563" cy="515" r="62"/>
      <circle class="rim" cx="563" cy="515" r="42"/>
      <circle class="hub" cx="563" cy="515" r="18"/>
      <circle class="tire" cx="1294" cy="515" r="62"/>
      <circle class="rim" cx="1294" cy="515" r="42"/>
      <circle class="hub" cx="1294" cy="515" r="18"/>
    </g>

    <ellipse cx="1085" cy="1050" rx="64" ry="64" fill="url(#pie-tone)" role="img" aria-label="Photo of golden hand pies"/>
    <text class="site-url" x="807" y="812" font-size="31" text-anchor="middle">MAPLEBROOKBAKES.COM</text>
    <text class="phone" x="812" y="1034" font-size="44" text-anchor="middle">(555) 014-0199</text>
    <text class="brand-name" x="1210" y="905" font-size="34" text-anchor="middle">MAPLEBROOK</text>
    <text class="brand-name" x="1210" y="947" font-size="34" text-anchor="middle">BAKES CO</text>
    <text class="tagline" x="1272" y="1042" font-size="15" text-anchor="middle">GOURMET PIES WITH A</text>
    <text class="tagline-script" x="1272" y="1074" font-size="40" text-anchor="middle">Southern Charm</text>
    <rect x="1180" y="1104" width="20" height="20" fill="var(--paper)"/>
    <text class="social-handle" x="1208" y="1121" font-size="17">@maplebrook</text>
  </g>

  <!-- Rear view -->
  <g class="bus-rear">
    <path class="body-shell" d="M1825,122 L2150,122 L2165,145 L2182,330 L2175,500 L1795,500 L1790,330 L1805,145 Z"/>
    <path d="M1825,122 L2150,122 L2165,145 L2180,318 L1792,318 L1805,145 Z" fill="url(#ray-glow-rear)"/>
    <path class="wrap-blue" d="M1792,330 Q1985,305 2180,318 L2175,475 L1795,475 Z"/>
    <rect class="black" x="1795" y="472" width="380" height="30"/>
    <rect class="black" x="1823" y="430" width="35" height="107" rx="12"/>
    <rect class="black" x="2100" y="430" width="35" height="107" rx="12"/>
    <ellipse cx="2115" cy="315" rx="42" ry="36" fill="url(#pie-tone)" role="img" aria-label="Photo of golden hand pies"/>
    <text class="site-url" x="1983" y="152" font-size="18" text-anchor="middle" letter-spacing="4">MAPLEBROOKBAKES.COM</text>
    <text class="brand-name" x="1985" y="230" font-size="30" text-anchor="middle">MAPLEBROOK</text>
    <text class="brand-name" x="1985" y="268" font-size="30" text-anchor="middle">BAKES CO</text>
    <text class="tagline" x="1983" y="358" font-size="14" text-anchor="middle">GOURMET PIES WITH A</text>
    <text class="tagline-script" x="1983" y="392" font-size="38" text-anchor="middle">Southern Charm</text>
    <text class="phone phone--light" x="1983" y="442" font-size="40" text-anchor="middle">(555) 014-0199</text>
  </g>

  <!-- Front view -->
  <g class="bus-front">
    <path class="body-shell" d="M1818,762 L2140,762 L2160,785 L2178,950 L2170,1125 L1790,1125 L1785,950 L1800,785 Z"/>
    <path class="body-shell" d="M1830,980 L1855,885 L2100,885 L2120,980 L2132,1080 L1828,1080 Z"/>
    <path d="M1848,965 L1865,890 L2095,890 L2115,965 Z" fill="var(--glass)"/>
    <path class="black" d="M1880,1022 L2080,1022 L2070,1055 L1890,1055 Z"/>
    <rect fill="#444" x="1895" y="1028" width="170" height="22" rx="11"/>
    <line class="outline" x1="1832" y1="1015" x2="2130" y2="1015"/>
    <rect fill="#f2e600" x="1824" y="1020" width="8" height="24"/>
    <rect fill="#f2e600" x="2128" y="1020" width="8" height="24"/>
    <path d="M1828,1068 L2132,1068 L2135,1130 L1825,1130 Z" fill="var(--bumper)"/>
    <rect class="black" x="1792" y="1115" width="375" height="32"/>
    <rect class="black" x="1823" y="1110" width="35" height="70" rx="12"/>
    <rect class="black" x="2100" y="1110" width="35" height="70" rx="12"/>
    <text class="brand-name" x="1980" y="818" font-size="18" text-anchor="middle">MAPLEBROOK</text>
    <text class="brand-name" x="1980" y="842" font-size="18" text-anchor="middle">BAKES CO</text>
    <text class="site-url" x="1980" y="996" font-size="22" text-anchor="middle" letter-spacing="1">MAPLEBROOKBAKES.COM</text>
  </g>
</svg>
</body>
</html>
```